Hair salon and Nail salon in Hawaii need a newspaper Ad design.

We need a newspaper Ad design for new open hair & nail salon in Waikiki Hawaii.Our Recommendation service for hair is "Head Spa" $30+tax and for nail is "Manicure Treatment Course" (Filing+Cuticle Care+Massage+Coloring) $20+tax.
We would like to see Hawaiian taste color and also having sense of luxury design. The ad size is W 5.0” x H 6.375”.
I would customers to know the shop place(Lanakila Crest Hotel 1F) , phone(808-555-0173), instagram(salonbrightwave) , our web site https://salonbrightwave.example and recommend services. For Web or Instagram , QR code is acceptable.

Target Market(s)

women & men

Industry/Entity Type

Beauty Salon

Font styles to use
Serif

Colors

Designer to choose colors to be used in the design.

Requirements
Must have
• Tagline for local customers. Shop Name is "SALON BRIGHTWAVE".the shop place(Lanakila Crest Hotel 1F) , phone(808-555-0173), instagram(salonbrightwave) and recommend services.
Nice to have
• Our services are competitive, but we don't want to be seen as just cheap and low quality.

```html
<!DOCTYPE html>
<html lang="en">
<head>
<meta charset="utf-8">
<title>Salon Brightwave — Newspaper Ad</title>
<link rel="stylesheet" href="https://fonts.googleapis.com/css2?family=Marcellus&family=Tinos:wght@700&display=swap">
<style>
  :root {
    --cocoa: #735452;
    --peach: #f2a266;
    --cream: #fff8f3;
    --blush: #f9e3d6;
    --white: #ffffff;
  }
  html, body { margin: 0; padding: 0; overflow: hidden; }
  body { width: 1200px; height: 941px; background: var(--cream); }
  .ad {
    position: relative; width: 1200px; height: 941px; overflow: hidden;
    font-family: "Marcellus", serif; color: var(--cocoa);
  }
  .backdrop {
    position: absolute; inset: 0;
    background:
      radial-gradient(ellipse at 50% 45%, #fffdfb 0%, rgba(255,253,251,0.9) 40%, rgba(255,253,251,0) 75%),
      linear-gradient(90deg, #f6d9c6 0%, var(--cream) 22%, var(--cream) 78%, #f6d9c6 100%);
  }
  .brand {
    position: absolute; top: 61px; left: 381px;
    display: flex; align-items: center; gap: 24px;
  }
  .brand-mark { width: 70px; height: 72px; background: var(--cocoa); }
  .brand-name { font-size: 37px; letter-spacing: 1px; line-height: 1; color: #4a3a3a; }
  .headline {
    position: absolute; top: 150px; left: 0; width: 1200px; margin: 0;
    text-align: center; font-weight: 400; font-size: 117px; line-height: 122px;
    letter-spacing: 1px;
  }
  .service { position: absolute; top: 436px; width: 292px; text-align: center; }
  .service--spa { left: 259px; }
  .service--nail { left: 651px; }
  .service-photo { width: 292px; height: 292px; border-radius: 50%; }
  .service--spa .service-photo { background: radial-gradient(circle at 55% 40%, #9a9a9a 0%, #cfcfcf 45%, #f4f4f4 85%, #ffffff 100%); }
  .service--nail .service-photo { background: radial-gradient(circle at 60% 55%, #f2c3a5 0%, #c9c3c9 45%, #6e6f86 75%, #e8e8ee 100%); }
  .service-name { margin: 0; font-weight: 400; line-height: 1; }
  .service--spa .service-name { font-size: 58px; margin-top: 6px; }
  .service--nail .service-name { font-size: 58px; margin-top: -10px; }
  .service-sub { font-size: 15px; letter-spacing: 4.2px; margin-top: 2px; }
  .service-price {
    font-family: "Tinos", serif; font-weight: 700; color: var(--peach);
    font-size: 40px; line-height: 1; margin-top: 8px;
  }
  .footer {
    position: absolute; left: 0; bottom: 0; width: 1200px; height: 80px;
    background: var(--cocoa); color: var(--white);
    display: flex; align-items: center; font-size: 26px;
  }
  .contact { position: absolute; display: flex; align-items: center; gap: 16px; }
  .contact--place { left: 155px; }
  .contact--phone { left: 558px; }
  .contact--social { left: 820px; }
  .contact svg { display: block; }
  .social-dot { width: 28px; height: 28px; border: 3px solid var(--white); border-radius: 50%; box-sizing: border-box; }
</style>
</head>
<body>
<main class="ad">
  <div class="backdrop" role="img" aria-label="Soft peach background with faded palm tree silhouettes"></div>

  <header class="brand">
    <div class="brand-mark"></div>
    <div class="brand-name">SALON BRIGHTWAVE</div>
  </header>

  <h1 class="headline">Are you ready for a<br>new &amp; better you?</h1>

  <section class="service service--spa">
    <div class="service-photo" role="img" aria-label="Hands lathering shampoo into hair during a head spa"></div>
    <h2 class="service-name">Head Spa</h2>
    <div class="service-price">$30+tax</div>
  </section>

  <section class="service service--nail">
    <div class="service-photo" role="img" aria-label="Manicured hands with dark polish beside a nail polish bottle and spa stones"></div>
    <h2 class="service-name">Manicure</h2>
    <div class="service-sub">TREATMENT COURSE</div>
    <div class="service-price">$20+tax</div>
  </section>

  <footer class="footer">
    <div class="contact contact--place">
      <svg width="22" height="34" viewBox="0 0 22 34" aria-hidden="true"><path d="M11 0C4.9 0 0 4.9 0 11c0 8 11 23 11 23s11-15 11-23C22 4.9 17.1 0 11 0zm0 15.5A4.5 4.5 0 1 1 11 6.5a4.5 4.5 0 0 1 0 9z" fill="#fff"/></svg>
      <span>Lanakila Crest Hotel 1F</span>
    </div>
    <div class="contact contact--phone">
      <svg width="24" height="40" viewBox="0 0 24 40" aria-hidden="true"><rect x="2" y="2" width="20" height="36" rx="3" fill="none" stroke="#fff" stroke-width="3"/><circle cx="12" cy="33" r="2" fill="#fff"/></svg>
      <span>808-555-0173</span>
    </div>
    <div class="contact contact--social">
      <div class="social-dot"></div>
      <span>salonbrightwave</span>
    </div>
  </footer>
</main>
</body>
</html>
```